Sign Shop website

We need a web design for a sign company called Quillby Signs that builds signs for shops such as A Frames, Banners, Tennet Boards, Shop front windows etc...

The existing site is avaliable at www.quillbysigns.com.au

We will need to have a fresh makeover. The new site must have the following:

Photo Galleries (broken down into sections)
Store Locations (currently there are 4 stores)
Online quote form
List of services
About Us Page

We just need to front page designed in photoshop (the inner page is not necessary) We have a team that can code the site up.

The website should have the exact logo. Any person who alters the logo, design will be elimated.

No Twitter, RSS, LinkedIn icons

The main colours are yellow, black, blue, red

Target Market(s)

Any business

Industry/Entity Type

It Company

Requirements
Must have
• jQuery slider banner
Should not have
• Alter the logo in any way

```html
<!DOCTYPE html>
<html lang="en">
<head>
<meta charset="utf-8">
<title>Quillby Signs &amp; Digital Printing</title>
<link href="https://fonts.googleapis.com/css2?family=Open+Sans:wght@300;400;600;700&display=swap" rel="stylesheet">
<style>
:root{
  --yellow:#efb22f;
  --red:#c8151b;
  --blue:#24469b;
  --ink:#333;
  --muted:#888;
  --rule:#ddd;
  --dark:#3b3b3b;
  --darker:#2f2f2f;
  --form:#333;
  --purple:#6a2a8e;
}
*{box-sizing:border-box;margin:0;padding:0}
html,body{width:1060px;height:1200px;overflow:hidden}
body{position:relative;font-family:"Open Sans",Arial,sans-serif;background:#fff;color:var(--ink)}
.abs{position:absolute}

.site-header{position:absolute;left:0;top:0;width:1060px;height:88px;background:var(--yellow)}
.brand{position:absolute;left:162px;top:22px;display:flex;align-items:center;gap:10px}
.brand-mark{width:26px;height:26px;background:var(--purple);border-radius:50%}
.brand-name{font-weight:700;font-size:28px;color:var(--purple);letter-spacing:-.5px}
.search{position:absolute;left:726px;top:18px;width:175px;height:26px;background:#fff;border:1px solid #ddd;font-size:8px;font-style:italic;color:#888;padding:7px 9px}
.search svg{position:absolute;right:6px;top:5px}
.main-nav{position:absolute;left:472px;top:62px;display:flex;font-size:11.5px;font-weight:600;color:#222}
.main-nav span{padding:0 20px;border-left:1px solid rgba(0,0,0,.15)}
.main-nav span:first-child{border-left:0;padding-left:0}
.main-nav span:last-child{padding-right:0}

.slider{position:absolute;left:151px;top:111px;width:759px;height:315px;background:linear-gradient(135deg,#c9c9c9,#ececec 45%,#bdbdbd);border-bottom:4px solid var(--yellow)}
.slide-photo{position:absolute;left:26px;top:25px;width:418px;height:252px;background:#fff;padding:6px;box-shadow:0 2px 6px rgba(0,0,0,.3)}
.slide-photo div{width:100%;height:100%;background:linear-gradient(180deg,#5a2a3e 0 16%,#2a2a30 16%,#6b5a5e 55%,#3a2f38)}
.slide-title{position:absolute;left:455px;top:33px;font-size:26px;line-height:34px;font-weight:300;color:var(--red);letter-spacing:-1px;white-space:nowrap}
.slide-text{position:absolute;left:456px;top:78px;width:290px;font-size:14.4px;line-height:25.6px;color:#333;letter-spacing:-.6px}
.btn-red{position:absolute;left:456px;top:253px;width:71px;height:28px;background:var(--red);color:#fff;font-size:12.5px;line-height:28px;text-align:center;border-radius:2px}
.dots{position:absolute;left:223px;top:291px;display:flex;gap:3px}
.dots i{width:7px;height:7px;border-radius:50%;background:#555}
.dots i:first-child{background:var(--red)}

.col-rule{position:absolute;top:461px;width:1px;height:281px;background:var(--rule)}
h2.section{position:absolute;font-size:19.5px;font-weight:600;color:#333;letter-spacing:-.5px}
.about-text{position:absolute;left:166px;top:492px;width:232px;font-size:10.6px;line-height:20.5px;color:var(--muted);letter-spacing:-.1px}
.btn-blue{position:absolute;height:20px;background:var(--blue);color:#fff;font-size:11px;line-height:20px;text-align:center;border-radius:3px;box-shadow:0 0 0 1px #8fa2cf}
.gallery-img{position:absolute;left:426px;width:208px;height:58px;border-radius:6px}
.quote-form{position:absolute;left:678px;top:496px;width:216px;height:213px;background:var(--form);border-radius:7px;padding:0 14px;color:#fff;font-size:10.5px}
.quote-form label{position:absolute;left:14px}
.quote-form .field{position:absolute;left:14px;width:188px;background:#fff;border:1px solid #999}

.services-rule{position:absolute;top:795px;height:1px;background:var(--rule)}
.service{position:absolute;top:838px;width:110px;text-align:center;font-size:10.8px;line-height:12px;color:var(--blue)}
.service .disc{width:86px;height:86px;margin:0 auto 10px;border-radius:50%;border:3px solid #fff;box-shadow:0 1px 5px rgba(0,0,0,.45)}

.site-footer{position:absolute;left:0;top:996px;width:1060px;height:164px;background:var(--dark)}
.footer-title{position:absolute;left:166px;top:12px;font-size:19px;font-weight:300;color:#fff;letter-spacing:-.5px}
.footer-rule{position:absolute;left:151px;top:49px;width:759px;height:1px;background:#4a4a4a}
.map{position:absolute;top:69px;width:71px;height:70px;background:linear-gradient(135deg,#e8e4d8,#d7dfcf)}
.store{position:absolute;top:66px;font-size:8.6px;line-height:12px;color:#8a8a8a}
.store h3{font-size:15px;font-weight:400;color:var(--red);line-height:18px;letter-spacing:-.4px}
.bottom-bar{position:absolute;left:0;top:1160px;width:1060px;height:40px;background:var(--darker);border-top:1px solid #222;font-size:8.4px;color:#999}
.bottom-bar nav{position:absolute;left:166px;top:14px;display:flex;gap:9px}
.bottom-bar p{position:absolute;right:155px;top:12px}
</style>
</head>
<body>

<header class="site-header">
  <div class="brand"><span class="brand-mark"></span><span class="brand-name">Quillby Signs</span></div>
  <div class="search">Enter your search here...
    <svg width="14" height="14" viewBox="0 0 14 14"><circle cx="6" cy="6" r="4.5" fill="none" stroke="#aaa" stroke-width="1.6"/><line x1="9.3" y1="9.3" x2="13" y2="13" stroke="#aaa" stroke-width="1.8"/></svg>
  </div>
  <nav class="main-nav"><span>Home</span><span>About Us</span><span>Our Services</span><span>Our Portfolio</span><span>Contact Us</span></nav>
</header>

<section class="slider">
  <div class="slide-photo"><div role="img" aria-label="Photo of a beauty salon shop front with window signage"></div></div>
  <h1 class="slide-title">Welcome to Quillby Signs</h1>
  <p class="slide-text">Le Lorem Ipsum est simplement du faux texte employé dans la composition et la mise en page avant impression. Le Lorem Ipsum est le faux texte standard de l'imprimerie depuis les années 1500, quand un peintre anonyme assembla ensemble des morceaux.</p>
  <div class="btn-red">Read More</div>
  <div class="dots"><i></i><i></i><i></i></div>
</section>

<h2 class="section" style="left:166px;top:455px">About Us</h2>
<p class="about-text">Quillby Signs is a Western Australian owned and managed company that was founded in 2005 and is fast becoming one of the state's leading manufacturer of quality signage.<br><br>Supplying signage for any application. Vinyl Computer Cut Lettering, Large Format Digital Print, Photo quality, Banners, Roster signs, Pull up Displays, Vehicle and Shop Windows. From small stickers to large format just to name a few.</p>
<div class="btn-blue" style="left:166px;top:723px;width:50px">More</div>

<div class="col-rule" style="left:404px"></div>
<div class="col-rule" style="left:657px"></div>

<h2 class="section" style="left:470px;top:455px">Image gallery</h2>
<svg class="abs" style="left:519px;top:498px" width="22" height="12" viewBox="0 0 22 12"><polyline points="2,10 11,2 20,10" fill="none" stroke="var(--yellow)" stroke-width="2.4"/></svg>
<div class="gallery-img" style="top:517px;background:linear-gradient(180deg,#a9b4c0,#d8d8d0 55%,#b79b86)" role="img" aria-label="Photo of a red triangle animal crossing road sign"></div>
<div class="gallery-img" style="top:585px;background:linear-gradient(180deg,#2a2a2a,#3a3322 50%,#c79a1e)" role="img" aria-label="Photo of yellow construction and hazard warning signs"></div>
<div class="gallery-img" style="top:653px;background:linear-gradient(90deg,#5c7aa8,#d8b21c 45%,#d8b21c 55%,#7e91ab)" role="img" aria-label="Photo of a yellow winding road sign held in hands"></div>
<svg class="abs" style="left:519px;top:718px" width="22" height="12" viewBox="0 0 22 12"><polyline points="2,2 11,10 20,2" fill="none" stroke="var(--yellow)" stroke-width="2.4"/></svg>

<h2 class="section" style="left:678px;top:455px">Online quote form</h2>
<form class="quote-form">
  <label style="top:16px">Name :</label>
  <div class="field" style="top:34px;height:25px"></div>
  <label style="top:70px">Email :</label>
  <div class="field" style="top:88px;height:25px"></div>
  <label style="top:124px">Comments :</label>
  <div class="field" style="top:142px;height:57px"></div>
</form>
<div class="btn-blue" style="left:829px;top:723px;width:50px">Submit</div>

<div class="services-rule" style="left:151px;width:325px"></div>
<h2 class="section" style="left:494px;top:781px">Services</h2>
<div class="services-rule" style="left:586px;width:323px"></div>

<div class="service" style="left:153px"><div class="disc" style="background:linear-gradient(180deg,#e9e9e9,#3a5f9c 55%,#1d1d1d)" role="img" aria-label="Photo of a vehicle decal"></div>Quality Stickers<br>&amp; Decals</div>
<div class="service" style="left:261px"><div class="disc" style="background:#3f7a5a" role="img" aria-label="Photo of a first aid box sign"></div>All Sign<br>Types</div>
<div class="service" style="left:367px"><div class="disc" style="background:linear-gradient(180deg,#aaa,#dcdcdc 55%,#888)" role="img" aria-label="Photo of a vehicle rear with signage"></div><br>Vehicle Signage</div>
<div class="service" style="left:475px"><div class="disc" style="background:linear-gradient(135deg,#c8923a,#3b3029 60%,#6c5a44)" role="img" aria-label="Photo of stacked magnets"></div><br>Magnets</div>
<div class="service" style="left:583px"><div class="disc" style="background:radial-gradient(circle,#e2b81c 0 30%,#f4f4f4 32%)" role="img" aria-label="Photo of a construction warning sign"></div>Construction and<br>safety Signs</div>
<div class="service" style="left:689px"><div class="disc" style="background:linear-gradient(180deg,#6d6f73,#cfd3d8 50%,#5c5f64)" role="img" aria-label="Photo of window lettering"></div><br>Window Signage</div>
<div class="service" style="left:796px"><div class="disc" style="background:linear-gradient(135deg,#7aa9c8,#dfe9ef 60%,#aac2d4)" role="img" aria-label="Photo of a laminated card"></div><br>Laminating</div>

<footer class="site-footer">
  <h2 class="footer-title">Store Locations</h2>
  <div class="footer-rule"></div>

  <div class="map" style="left:166px" role="img" aria-label="Street map of the Harrowdale store"></div>
  <div class="store" style="left:255px"><h3>Harrowdale</h3>Unit 5, 40-46 Fenwick Avenue<br>Harrowdale, WA 6999<br><br>Phone: (08) 5550 0142<br>Fax: (08) 5550 0143</div>

  <div class="map" style="left:424px" role="img" aria-label="Street map of the Kestrel Bay store"></div>
  <div class="store" style="left:515px"><h3>Kestrel Bay</h3>Shop 3, 91 Tarn Promenade,<br>Kestrel Bay, W.A<br><br>Phone: 08 5550 0188</div>

  <div class="map" style="left:682px" role="img" aria-label="Street map of the Marlow Lakes store"></div>
  <div class="store" style="left:772px"><h3>Marlow Lakes</h3>Unit 5, 40-46 Fenwick Avenue<br>Harrowdale, WA 6999<br><br>Phone: (08) 5550 0142<br>Fax: (08) 5550 0143</div>
</footer>

<div class="bottom-bar">
  <nav><span>Home</span><span>About Us</span><span>Our Services</span><span>Our Portfolio</span><span>Contact Us</span></nav>
  <p>© Copyrights 2013 All rights Reserved</p>
</div>

</body>
</html>
```